Zielgruppe
WIr sind ein klassisches Immobilienmaklerbüro für private Wohnimmobilien. Die Zielgruppe sind somit sowohl Verkäufer (i.d.R. gut situiert, 50-70 Jahre) als auch Käufer und Interessenten (20-35 Jahre).
Aufgabenstellung
Das Desgin soll seriös, vertrauenswürdig aber dennoch modern und dynamisch sein. Ich vollziehe aktuell einen Designwechsel und bin von einem schwarzen Design (www.wohn-punkt.example) auf ein helles Deisgn (http://wohnpunkt.de.xq48213.hostbeispiel.example/) umgestiegen. Die Visitenkarte soll zum neuen Design passen. Ein Bild von mir ist nicht gewünscht. Ob die Rückseite der Karten genutzt werden soll weiß ich selbst noch nicht. Wenn jemand eine sinnvolle Verwendung hat, bin ich dafür gerne offen.

```html
<!DOCTYPE html>
<html lang="de">
<head>
<meta charset="utf-8">
<title>WohnPunkt – Visitenkarte</title>
<link rel="stylesheet" href="https://fonts.googleapis.com/css2?family=Arimo:wght@400;700&family=Open+Sans:wght@400;700;800&display=swap">
<style>
  :root {
    --page: #e9e6e1;
    --card: #f1f5f3;
    --green: #6fac1f;
    --green-light: #80bb2c;
    --ink: #1c1c1c;
    --ink-soft: #3a3a3a;
    --white: #ffffff;
  }
  * { box-sizing: border-box; margin: 0; padding: 0; }
  html, body { width: 1200px; height: 800px; overflow: hidden; }
  body {
    background: var(--page);
    font-family: "Arimo", Arial, sans-serif;
    position: relative;
  }
  .card {
    position: absolute;
    top: 232px;
    width: 520px;
    height: 336px;
    background: var(--card);
    box-shadow: 0 6px 22px rgba(0,0,0,0.18);
    overflow: hidden;
  }
  .card--front { left: 45px; }
  .card--back { left: 635px; }

  .green-field {
    position: absolute;
    overflow: hidden;
    background: linear-gradient(135deg, var(--green) 0%, var(--green-light) 55%, var(--green) 100%);
  }
  .card--front .green-field { left: 264px; top: 18px; right: 18px; bottom: 18px; }
  .card--back .green-field { left: 18px; top: 18px; right: 18px; bottom: 18px; }

  /* front, personal side */
  .person { position: absolute; left: 26px; top: 34px; }
  .person__name {
    font-family: "Open Sans", sans-serif;
    font-size: 23px;
    letter-spacing: -0.5px;
    color: var(--ink-soft);
    line-height: 1;
  }
  .person__name strong { font-weight: 800; color: var(--ink); }
  .person__role {
    display: block;
    margin-top: 3px;
    background: var(--green);
    color: var(--white);
    font-family: "Open Sans", sans-serif;
    font-size: 17px;
    padding: 0 12px 1px 44px;
    width: 226px;
  }
  .person__degree {
    font-family: "Open Sans", sans-serif;
    font-size: 10px;
    color: var(--ink-soft);
    margin: 3px 0 0 66px;
  }
  .contact {
    position: absolute;
    left: 26px;
    bottom: 24px;
    font-weight: 700;
    font-variant: small-caps;
    font-size: 12.5px;
    letter-spacing: 1px;
    line-height: 1.3;
    color: var(--ink);
    white-space: nowrap;
  }

  /* brand lockup */
  .brand {
    display: flex;
    align-items: center;
    gap: 10px;
    font-family: "Arimo", Arial, sans-serif;
    font-variant: small-caps;
    color: var(--ink);
    white-space: nowrap;
  }
  .brand__mark { background: var(--ink); flex: none; }
  .card--front .brand {
    position: absolute; right: 18px; top: 62px;
    font-size: 20px;
    letter-spacing: 3px;
  }
  .card--front .brand__mark { width: 34px; height: 34px; }
  .company {
    position: absolute;
    left: 16px; bottom: 20px;
    color: var(--white);
    font-weight: 700;
    font-variant: small-caps;
    font-size: 10.5px;
    letter-spacing: 0.6px;
    line-height: 1.35;
    white-space: nowrap;
  }

  /* back side */
  .card--back .brand {
    position: absolute; left: 0; right: 0; top: 96px;
    justify-content: center;
    font-size: 40px;
    letter-spacing: 7px;
  }
  .card--back .brand__mark { width: 62px; height: 62px; }
  .tagline {
    position: absolute; left: 0; right: 0; top: 190px;
    text-align: center;
    color: var(--white);
    font-variant: small-caps;
    font-size: 15px;
    letter-spacing: 2px;
  }
  .web {
    position: absolute; left: 0; right: 0; top: 248px;
    text-align: center;
    color: var(--white);
    font-weight: 700;
    font-variant: small-caps;
    font-size: 13px;
    letter-spacing: 2px;
  }
</style>
</head>
<body>

  <section class="card card--front" aria-label="Visitenkarte Vorderseite">
    <div class="person">
      <p class="person__name"><strong>JONAS</strong> BERGER</p>
      <span class="person__role">Geschäftsführer</span>
      <p class="person__degree">Betriebswirt (VWA)</p>
    </div>
    <p class="contact">
      Tel.: +49 7000 41526-23<br>
      Fax: +49 7000 41526-24<br>
      Mobil: +49 170 0004817<br>
      Email: berger@wohn-punkt.example
    </p>
    <div class="green-field" role="img" aria-label="Grüne Fläche mit feinem Flechtmuster">
      <div class="brand"><span class="brand__name">WohnPunkt</span><span class="brand__mark"></span></div>
      <p class="company">
        info@wohn-punkt.example<br>
        http://www.wohn-punkt.example<br>
        WohnPunkt Immobilien GmbH<br>
        Eschweg 9, 73035 Musterstadt
      </p>
    </div>
  </section>

  <section class="card card--back" aria-label="Visitenkarte Rückseite">
    <div class="green-field" role="img" aria-label="Grüne Fläche mit feinem Flechtmuster">
      <div class="brand"><span class="brand__name">WohnPunkt</span><span class="brand__mark"></span></div>
      <p class="tagline">Realty Point Immobilien GmbH</p>
      <p class="web">wohnpunkt.example</p>
    </div>
  </section>

</body>
</html>
```